Landing Page and Logo for Auto-Blogging Platform

I created a platform that allows users to start a blog for their business, hobby, charity, etc. I need a landing page where users can learn about the platform, benefits of consistent blogging, SEO value, plans/pricing, etc. The landing page needs to have multiple call to action buttons encouraging the visitor to register/sign up for a free trial.

In addition to the landing page, I need a page for users to establish the settings for their blog. This page should be a fairly simple form, intended for the user to enter a few details to set up their blog:
1. Name of Blog
2. Up to 10 topics and/or keywords the blog should focus on
3. Theme: Color-scheme and logo upload for blog.

I have attached the specifications of the platform's functionality so you can better understand how it works, plans/pricing, etc.

I also need a logo for the business. The name of the platform is PennaWave.

Target Market(s)

Website owners, bloggers, business owners

Industry/Entity Type

Technology, Internet, web design

Coding

Coded - Design and coding required

Number of Pages Required

2 page

Colors
0054AA
0677BA
7BADD7
CADEEF
E8F1F8
0094D4
00A9DD
6FCCEA
C7EBF8
E9F6FB

Requirements
Must have
• Eye-catching design but fairly light on content (keep it simple and brief.)
Nice to have
• Eye-catching yet simple design, clean and easy to understand what we are offering.
Should not have
• Too much “wordy” and confusing content.

```html
<!DOCTYPE html>
<html lang="en">
<head>
<meta charset="utf-8">
<title>PennaWave – Automate Your Blog Posting with AI</title>
<link href="https://fonts.googleapis.com/css2?family=Plus+Jakarta+Sans:wght@400;500;600;700;800&family=Oswald:wght@400;500&display=swap" rel="stylesheet">
<style>
:root{
  --blue:#5178f0;
  --blue-deep:#3d62e0;
  --ink:#161a2c;
  --body:#2a2e40;
  --muted:#6b7085;
  --pale:#e3eafb;
  --sky:#e9f6fb;
  --sky2:#cadeef;
  --line:#e6e8ef;
  --night:#0d1526;
  --white:#ffffff;
}
*{box-sizing:border-box;margin:0;padding:0}
html,body{width:1200px;height:3257px;overflow:hidden}
body{position:relative;background:var(--white);font-family:"Plus Jakarta Sans",sans-serif;color:var(--ink)}
.abs{position:absolute}
.accent{color:var(--blue)}
.logo{font-weight:800;font-size:34px;letter-spacing:-0.5px;color:var(--ink)}
.logo .accent{color:var(--blue)}
.btn{display:inline-flex;align-items:center;gap:10px;background:var(--blue);color:var(--white);font-weight:700;font-size:14px;border-radius:30px;padding:0 14px;height:37px;white-space:nowrap}
.btn .dot{width:15px;height:15px;border-radius:50%;background:var(--white);display:inline-flex;align-items:center;justify-content:center}
.btn .dot svg{width:9px;height:9px}
.art{border-radius:14px}

/* header */
.site-header{left:0;top:0;width:1200px;height:81px;border-bottom:1px solid var(--line);background:var(--white)}
.site-header .logo{left:85px;top:17px}
.nav{left:417px;top:30px;display:flex;gap:29px;font-size:15px;font-weight:500;color:var(--body)}
.site-header .btn{left:881px;top:20px;width:230px;justify-content:center}

/* hero */
.hero{left:0;top:81px;width:1200px;height:519px;background:linear-gradient(100deg,#edf3fd 0%,#dcebfa 45%,#e8f4fc 100%)}
.eyebrow{font-size:19px;font-weight:500;color:var(--ink)}
.h1{font-size:43px;font-weight:800;line-height:51px;letter-spacing:-0.6px}
.lead{font-size:16px;line-height:24px;color:var(--body);font-weight:500}
.signup{display:flex;align-items:center;justify-content:space-between;background:var(--white);border-radius:30px;height:45px;padding:0 4px 0 20px}
.signup span{font-size:14px;color:#9a9fb0}
.signup .btn{height:37px}

/* steps */
.steps{left:0;top:600px;width:1200px;height:89px;background:var(--blue)}
.step{position:absolute;top:0;height:89px;border-radius:0 45px 45px 0;display:flex;align-items:center}
.step.light{background:#e2e9fb;color:var(--ink)}
.step.dark{background:var(--blue);color:var(--white)}
.step .num{font-family:"Oswald",sans-serif;font-size:19px;line-height:25px;text-align:center;width:42px;padding-right:10px;border-right:1.5px solid currentColor;margin-right:14px}
.step.light .num{color:var(--blue)}
.step .txt{font-size:14px;font-weight:600;line-height:19px}
.step .txt small{display:block;font-size:10.5px;font-weight:500;margin-top:4px}

/* about */
.about-text{left:647px;top:785px;width:450px}
.h2{font-size:43px;font-weight:800;letter-spacing:-0.6px;line-height:52px}

/* seo */
.seo{left:86px;top:1129px;width:1027px;height:243px;border-radius:24px;background:linear-gradient(95deg,#dbeafb 0%,#eef5fc 55%,#e4f1fa 100%)}

/* benefits */
.cards{left:86px;top:1559px;width:1027px;height:237px}
.card{position:absolute;top:0;height:237px;border:1px solid var(--line);border-radius:6px;background:#fdfcfc;padding:76px 22px 0}
.card h3{font-size:19px;font-weight:800;line-height:23px}
.card p{font-size:11px;line-height:17px;color:var(--body);margin-top:10px}
.card .arrow{position:absolute;left:22px;top:198px;width:16px;height:12px}
.card.active{background:var(--blue);border-color:var(--blue);color:var(--white)}
.card.active p{color:var(--white)}

/* plans */
.plan{position:absolute;top:2113px;width:323px;height:384px;background:var(--white);border-radius:4px;box-shadow:0 4px 16px rgba(30,40,90,.07);text-align:center}
.plan header{height:77px;background:#e4ebfb;display:flex;align-items:center;justify-content:center;font-size:23px;font-weight:700;border-radius:4px 4px 0 0}
.plan.top header{background:var(--blue);color:var(--white)}
.plan .feat{font-size:19px;line-height:28px;margin-top:21px;color:var(--ink)}
.plan .feat b{font-weight:700}
.plan .price{position:absolute;left:0;right:0;top:232px;font-size:31px;font-weight:800;color:var(--blue)}
.plan .start{position:absolute;left:50%;top:296px;transform:translateX(-50%);width:126px;height:38px;border:1.5px solid var(--ink);border-radius:20px;display:flex;align-items:center;justify-content:center;gap:8px;font-size:14px;font-weight:600}
.plan .start i{width:15px;height:15px;border-radius:50%;background:var(--ink);display:inline-flex;align-items:center;justify-content:center}

.pay{top:2676px;left:0;width:1200px;display:flex;justify-content:center;gap:46px;font-size:32px;font-weight:700;color:#1f2a4d;letter-spacing:-0.5px}

/* cta */
.footer-band{left:0;top:3041px;width:1200px;height:216px;background:var(--night)}
.cta{left:86px;top:2788px;width:1027px;height:320px;border-radius:24px;background:linear-gradient(100deg,#e2edfb 0%,#eef6fc 55%,#dff0f8 100%)}
.site-footer .logo{color:var(--white)}
.social{display:flex;gap:10px}
.social span{width:23px;height:23px;border-radius:50%;background:var(--white)}
</style>
</head>
<body>

<header class="abs site-header">
  <div class="abs logo">Penna<span class="accent">Wave</span></div>
  <nav class="abs nav"><span>Features</span><span>Integrations</span><span>Pricing</span><span>Contact us</span></nav>
  <a class="abs btn">Start your free blog today! <span class="dot"><svg viewBox="0 0 10 10"><path d="M2 5h6M5 2l3 3-3 3" stroke="#5178f0" stroke-width="1.6" fill="none"/></svg></span></a>
</header>

<section class="abs hero">
  <div class="abs eyebrow" style="left:85px;top:96px">Introducing Auto Blogging</div>
  <h1 class="abs h1" style="left:85px;top:147px"><span class="accent">Automate</span> Your<br>Blog Posting with AI</h1>
  <p class="abs lead" style="left:85px;top:272px;width:420px">The purpose of this platform is to allow anyone to start a blog and automate the process of creating content and posting it to the blog.</p>
  <div class="abs signup" style="left:85px;top:384px;width:461px">
    <span>Your@email.com</span>
    <a class="btn">Start your free blog today! <span class="dot"><svg viewBox="0 0 10 10"><path d="M2 5h6M5 2l3 3-3 3" stroke="#5178f0" stroke-width="1.6" fill="none"/></svg></span></a>
  </div>
  <div class="abs art" role="img" aria-label="Illustration of a person working on a laptop beside an AI assistant screen, gears and folder icons" style="left:613px;top:64px;width:493px;height:361px;background:linear-gradient(135deg,rgba(81,120,240,.18),rgba(202,222,239,.45))"></div>
</section>

<section class="abs steps">
  <div class="step dark" style="left:0;width:1200px;padding-left:998px"></div>
  <div class="step light" style="left:0;width:895px;padding-left:0"></div>
  <div class="step dark" style="left:0;width:578px"></div>
  <div class="step light" style="left:0;width:314px"></div>

  <div class="step" style="left:42px;background:none;color:var(--ink)"><div class="num" style="color:var(--blue)">STEP<br>01</div><div class="txt">Select frequency of<br>Automated Blog Posts<small>(Daily, weekly, or monthly)</small></div></div>
  <div class="step" style="left:344px;background:none;color:var(--white)"><div class="num">STEP<br>02</div><div class="txt">Give a Custom<br>Name your blog<small>(Choose your Blog name)</small></div></div>
  <div class="step" style="left:616px;background:none;color:var(--ink)"><div class="num" style="color:var(--blue)">STEP<br>03</div><div class="txt">Select your blog topics<br>as per your own choice<small>(or let AI choose them for you)</small></div></div>
  <div class="step" style="left:928px;background:none;color:var(--white)"><div class="num">STEP<br>04</div><div class="txt">You are free to do<br>someting else<small>(or let AI choose them for you)</small></div></div>
</section>

<section>
  <div class="abs art" role="img" aria-label="Illustration of a person with a laptop in front of a large screen showing images, text and a video player" style="left:114px;top:765px;width:420px;height:285px;background:linear-gradient(135deg,#eef2fd,#dbe5fb)"></div>
  <div class="abs about-text">
    <div class="eyebrow">Introducing Auto Blogging</div>
    <h2 class="h2" style="margin-top:18px"><span class="accent">About</span> the platform</h2>
    <p class="lead" style="margin-top:24px;font-weight:400">Lorem Ipsum is simply dummy text of the printing and typesetting industry. Lorem Ipsum has been the industry's standard dummy text ever since the 1500s, when an unknown printer took a galley of type and scrambled it to make a type specimen book. It has survived not only five centuries.</p>
  </div>
</section>

<section class="abs seo">
  <h2 class="abs h2" style="left:63px;top:47px"><span class="accent">Improving</span> SEO results</h2>
  <p class="abs lead" style="left:66px;top:118px;width:450px;font-weight:400">Constantly posting fresh, new, keyword-targeted content to their website or blog will help to increase the page ranking in Search Engine Optimization.</p>
  <div class="abs art" role="img" aria-label="Illustration of a person at a desk with a laptop in front of an analytics dashboard" style="left:654px;top:21px;width:297px;height:200px;background:linear-gradient(135deg,rgba(81,120,240,.2),rgba(255,255,255,.5))"></div>
</section>

<h2 class="abs h2" style="left:0;top:1460px;width:1200px;text-align:center">How <span class="accent">Autoblogging</span> Can Help Your Brand</h2>

<section class="abs cards">
  <article class="card" style="left:0;width:244px"><h3>100%<br>Automated Content</h3><p>Lorem Ipsum is simply dummy text of the printing and typesetting industry. Lorem Ipsum has been.</p><svg class="arrow" viewBox="0 0 16 12"><path d="M1 6h13M9 1l5 5-5 5" stroke="currentColor" stroke-width="1.4" fill="none"/></svg></article>
  <article class="card active" style="left:262px;width:245px"><h3>Easy<br>configuration</h3><p>Lorem Ipsum is simply dummy text of the printing and typesetting industry. Lorem Ipsum has been.</p><svg class="arrow" viewBox="0 0 16 12"><path d="M1 6h13M9 1l5 5-5 5" stroke="currentColor" stroke-width="1.4" fill="none"/></svg></article>
  <article class="card" style="left:521px;width:244px"><h3>Relevant<br>content</h3><p>Lorem Ipsum is simply dummy text of the printing and typesetting industry. Lorem Ipsum has been.</p><svg class="arrow" viewBox="0 0 16 12"><path d="M1 6h13M9 1l5 5-5 5" stroke="currentColor" stroke-width="1.4" fill="none"/></svg></article>
  <article class="card" style="left:784px;width:243px"><h3>Pressly<br>Integration</h3><p>Lorem Ipsum is simply dummy text of the printing and typesetting industry. Lorem Ipsum has been.</p><svg class="arrow" viewBox="0 0 16 12"><path d="M1 6h13M9 1l5 5-5 5" stroke="currentColor" stroke-width="1.4" fill="none"/></svg></article>
</section>

<a class="abs btn" style="left:485px;top:1847px;width:230px;justify-content:center">Start your free blog today! <span class="dot"><svg viewBox="0 0 10 10"><path d="M2 5h6M5 2l3 3-3 3" stroke="#5178f0" stroke-width="1.6" fill="none"/></svg></span></a>

<div class="abs eyebrow" style="left:0;top:1974px;width:1200px;text-align:center">Plans &amp; Pricing</div>
<h2 class="abs h2" style="left:0;top:2012px;width:1200px;text-align:center">Our <span class="accent">Subscriptions</span> Plans</h2>

<article class="plan" style="left:86px">
  <header>Base Plan</header>
  <p class="feat">1 blog post<br>(up to <b>2,000 words</b>)<br>every month</p>
  <div class="price">$9.99/month</div>
  <a class="start">Start Now <i><svg width="9" height="9" viewBox="0 0 10 10"><path d="M2 5h6M5 2l3 3-3 3" stroke="#fff" stroke-width="1.6" fill="none"/></svg></i></a>
</article>
<article class="plan" style="left:437px">
  <header>Premium Plan</header>
  <p class="feat">1 blog post<br>(up to <b>2,000 words</b>)<br>every week</p>
  <div class="price">$14.99/month</div>
  <a class="start">Start Now <i><svg width="9" height="9" viewBox="0 0 10 10"><path d="M2 5h6M5 2l3 3-3 3" stroke="#fff" stroke-width="1.6" fill="none"/></svg></i></a>
</article>
<article class="plan top" style="left:790px">
  <header>Ultimate Plan</header>
  <p class="feat">1 blog post<br>(up to <b>3,000 words</b>)<br>per day plus unlimited<br>manual posting</p>
  <div class="price">$24.99/month</div>
  <a class="start">Start Now <i><svg width="9" height="9" viewBox="0 0 10 10"><path d="M2 5h6M5 2l3 3-3 3" stroke="#fff" stroke-width="1.6" fill="none"/></svg></i></a>
</article>

<p class="abs" style="left:0;top:2548px;width:1200px;text-align:center;font-size:17px;line-height:25px;color:var(--body);font-weight:500">The platform can be used to sell unique accounts to multiple users.<br>There must be a subscription plan and a <b class="accent">14-day free trial</b>.</p>

<div class="abs pay"><span>Strivo</span><span>PayNest</span><span>Orchard Pay</span><span>Gleam Pay</span><span>Amberly Pay</span></div>

<div class="abs footer-band"></div>
<section class="abs cta">
  <h2 class="abs" style="left:66px;top:36px;font-size:51px;font-weight:800;line-height:60px;letter-spacing:-0.8px"><span class="accent">Automate</span><br>your Blog today</h2>
  <p class="abs lead" style="left:66px;top:176px">Get your samples and start generating articles for your business.</p>
  <div class="abs signup" style="left:66px;top:228px;width:461px">
    <span>Your@email.com</span>
    <a class="btn">Start your free blog today! <span class="dot"><svg viewBox="0 0 10 10"><path d="M2 5h6M5 2l3 3-3 3" stroke="#5178f0" stroke-width="1.6" fill="none"/></svg></span></a>
  </div>
  <div class="abs art" role="img" aria-label="Illustration of a person pointing at a browser window with a video player and an AI head icon" style="left:597px;top:25px;width:373px;height:272px;background:linear-gradient(135deg,rgba(81,120,240,.2),rgba(255,255,255,.5))"></div>
</section>

<footer class="site-footer">
  <div class="abs logo" style="left:85px;top:3165px">Penna<span class="accent">Wave</span></div>
  <div class="abs" style="left:0;top:3177px;width:1200px;text-align:center;color:var(--white);font-size:15px;font-weight:500">Copyright © 2024 PennaWave. All Rights Reserved.</div>
  <div class="abs social" style="left:1023px;top:3175px"><span></span><span></span><span></span></div>
</footer>

</body>
</html>
```